Corporate Business Card

Very professional, Modern, Not to busy, include phone address email, website
(253) 555-0174, 61807 19th Street N, Kent, WA 98517, marcus@kestrelbayholding.com, brelvanindustries.com

Target Market(s)

Manufacturing

Industry/Entity Type

Aero, machining, manufacturing, Off road racing

Contact Information for Business Card

Phone, address email, website

```html
<!DOCTYPE html>
<html lang="en">
<head>
<meta charset="utf-8">
<title>Brelvan Industries — Business Card</title>
<link rel="stylesheet" href="https://fonts.googleapis.com/css2?family=Saira:wght@500;700&family=Noto+Sans:wght@400&display=swap">
<style>
  :root {
    --backdrop: #8a8b8e;
    --card-white: #ffffff;
    --brand-navy: #12337a;
    --brand-red: #e21e2d;
    --ink-navy: #17346f;
  }
  * { box-sizing: border-box; margin: 0; padding: 0; }
  html, body {
    width: 1200px; height: 781px; overflow: hidden;
    background: var(--backdrop);
  }
  .canvas {
    width: 1200px; height: 781px;
    display: flex; align-items: center; justify-content: center; gap: 40px;
  }
  .card {
    width: 540px; height: 309px;
    position: relative;
    box-shadow: 0 10px 24px rgba(0,0,0,0.28);
  }
  .card-front { background: var(--card-white); }
  .card-back {
    background: var(--brand-navy);
    display: flex; align-items: center; justify-content: center;
  }

  .contact-block { position: absolute; left: 44px; top: 44px; }
  .person-name {
    font-family: 'Saira', sans-serif; font-weight: 700;
    font-size: 21px; letter-spacing: 0.5px; line-height: 1;
    color: var(--ink-navy); text-transform: uppercase;
  }
  .person-name .first { color: var(--brand-red); }
  .person-role {
    font-family: 'Noto Sans', sans-serif; font-size: 11px;
    color: var(--ink-navy); margin-top: 5px;
  }
  .contact-list { list-style: none; margin-top: 14px; }
  .contact-list li {
    display: flex; align-items: center; gap: 7px;
    font-family: 'Noto Sans', sans-serif; font-size: 12.5px;
    color: var(--ink-navy); line-height: 1.7;
  }
  .contact-list svg { width: 11px; height: 11px; flex: none; }

  .divider {
    position: absolute; left: 44px; top: 176px;
    width: 330px; height: 1.5px; background: var(--brand-red);
  }

  .brand {
    font-family: 'Saira', sans-serif; font-weight: 700;
    display: flex; align-items: center; gap: 10px;
  }
  .brand-mark { width: 14px; height: 14px; background: var(--brand-red); }
  .card-front .brand {
    position: absolute; right: 40px; top: 96px;
    font-size: 24px; color: var(--brand-navy);
  }
  .card-back .brand { font-size: 34px; color: var(--card-white); }

  .address {
    position: absolute; right: 44px; bottom: 40px; text-align: right;
    font-family: 'Noto Sans', sans-serif; font-size: 12.5px;
    line-height: 1.6; color: var(--ink-navy);
  }
</style>
</head>
<body>
<main class="canvas">
  <section class="card card-front">
    <div class="contact-block">
      <p class="person-name"><span class="first">Marcus</span> Orvane</p>
      <p class="person-role">Director</p>
      <ul class="contact-list">
        <li>
          <svg viewBox="0 0 12 12" aria-hidden="true"><path d="M2.5 1h2l1 2.8-1.3 1a6 6 0 0 0 3 3l1-1.3L11 7.5v2A1.5 1.5 0 0 1 9.5 11 8.5 8.5 0 0 1 1 2.5 1.5 1.5 0 0 1 2.5 1z" fill="#e21e2d"/></svg>
          (253) 555-0174
        </li>
        <li>
          <svg viewBox="0 0 12 12" aria-hidden="true"><rect x="0.5" y="2" width="11" height="8" rx="1" fill="#e21e2d"/><path d="M1 2.5l5 4 5-4" stroke="#fff" stroke-width="1" fill="none"/></svg>
          marcus@kestrelbayholding.com
        </li>
        <li>
          <svg viewBox="0 0 12 12" aria-hidden="true"><circle cx="6" cy="6" r="5.2" fill="none" stroke="#e21e2d" stroke-width="1.2"/><ellipse cx="6" cy="6" rx="2.2" ry="5.2" fill="none" stroke="#e21e2d" stroke-width="1"/><path d="M1 6h10" stroke="#e21e2d" stroke-width="1"/></svg>
          brelvanindustries.com
        </li>
      </ul>
    </div>

    <div class="brand"><span class="brand-mark"></span><span>Brelvan Industries</span></div>

    <div class="divider"></div>

    <address class="address" style="font-style:normal">
      61807 19th Street N<br>
      Kent, WA 98517
    </address>
  </section>

  <section class="card card-back">
    <div class="brand"><span class="brand-mark"></span><span>Brelvan Industries</span></div>
  </section>
</main>
</body>
</html>
```